Labor & Delivery Medical Device Quick Reference Guide

We need a quick reference guide updated for a labor and delivery medical device. The content of the piece is in the old sales sheet.

You can learn about the product here: www.velacheckkit.com

I have uploaded the old design.

I am looking for something bright, attractive, clean. The old design is old and boring.

You do not need to use the colors in the logos that I have attached but the logos do need to be on the document. Vela Kit is the product and Harbor Medica is the manufacturer.

Target Market(s)

Nurses on the labor and delivery floor
Lab techs in hospital laboratories
Obstetricians

Industry/Entity Type

Medical Equipment

Colors
ffffff

Requirements
Must have
• Must have the content from the old design. Content meaning all the words and images.
Nice to have
• The content is most important but the design needs to support the content. The design needs to be bright and attractive.

```html
<!DOCTYPE html>
<html lang="en">
<head>
<meta charset="utf-8">
<title>Vela Kit Inservice Guides</title>
<link href="https://fonts.googleapis.com/css2?family=Open+Sans:wght@400;600;700&display=swap" rel="stylesheet">
<style>
:root{
  --page:#ffffff;
  --band:#efefef;
  --ink:#5d6a73;
  --ink-soft:#7b868d;
  --green:#7cc242;
  --blue:#2a6fb0;
  --art:#d9dde0;
  --shadow:rgba(0,0,0,.28);
}
*{margin:0;padding:0;box-sizing:border-box}
html,body{width:1200px;height:837px;overflow:hidden;background:var(--page)}
body{position:relative;font-family:"Open Sans",Arial,sans-serif;color:var(--ink)}
.sheet{position:absolute;top:65px;width:502px;height:708px;background:var(--page);box-shadow:2px 3px 6px var(--shadow);overflow:hidden}
.sheet--poc{left:100px}
.sheet--lab{left:672px}
.band{position:absolute;left:0;width:100%}
.band--grey{background:var(--band)}
.band--white{background:var(--page)}
.notch{position:absolute;left:50%;bottom:-9px;margin-left:-9px;width:0;height:0;border-left:9px solid transparent;border-right:9px solid transparent;border-top:9px solid var(--band);z-index:2}
.band--white .notch{border-top-color:var(--page)}
.title{position:absolute;left:28px;font-size:21px;font-weight:400;color:var(--ink);letter-spacing:-.2px}
.title strong{color:var(--green);font-weight:700}
.step{position:absolute;right:28px;text-align:right;font-size:11.5px;line-height:16px;color:var(--ink)}
.art{position:absolute;background:var(--art);border-radius:3px}
.brand{position:absolute;display:flex;align-items:center;gap:5px;font-size:20px;font-weight:600;color:var(--blue);white-space:nowrap}
.brand .dot{width:13px;height:13px;border-radius:50%;background:var(--blue)}
.brand-sub{position:absolute;font-size:6px;font-weight:600;color:var(--ink-soft)}
.bracket{position:absolute;border-color:var(--green);border-style:solid;border-width:0;z-index:4}
.warning{position:absolute;left:32px;width:336px;font-size:7.5px;line-height:11px;color:var(--ink)}
.foot-links{position:absolute;left:32px;top:645px;font-size:8.5px;font-weight:700;color:var(--green)}
.foot-info{position:absolute;left:32px;top:664px;font-size:6.5px;line-height:10px;color:var(--ink)}
.maker{position:absolute;left:388px;top:655px;display:flex;align-items:center;gap:5px;font-size:10px;font-weight:700;color:var(--green);white-space:nowrap}
.maker .dot{width:13px;height:13px;border-radius:50%;background:var(--green)}
.tagline{position:absolute;left:388px;top:680px;width:100px;font-size:6.5px;line-height:9px;font-weight:600;color:var(--ink)}
</style>
</head>
<body>

<section class="sheet sheet--poc" aria-label="Inservice Guide Point of Care">
  <div class="band band--grey" style="top:0;height:120px">
    <h1 class="title" style="top:45px">Inservice Guide -<strong>Point of Care</strong></h1>
    <div class="notch"></div>
  </div>
  <div class="bracket" style="left:374px;top:14px;width:32px;height:32px;border-top-width:2px;border-left-width:2px"></div>
  <div class="art" role="img" aria-label="Photo of the Vela Kit test cassette with timer button" style="left:383px;top:23px;width:85px;height:138px;background:#eceef0;z-index:3;box-shadow:0 1px 3px rgba(0,0,0,.25)"></div>
  <div class="bracket" style="left:445px;top:129px;width:28px;height:44px;border-bottom-width:2px;border-right-width:2px"></div>

  <div class="band band--white" style="top:120px;height:118px">
    <div class="art" role="img" aria-label="Drawing of a hand removing the cap from the buffer vial" style="left:32px;top:30px;width:50px;height:50px"></div>
    <p class="step" style="top:70px">Remove contents from package. Holding the buffer vial<br>in an upright position, remove the shipping cap as shown<br>and set the vial aside</p>
    <div class="notch"></div>
  </div>
  <div class="band band--grey" style="top:238px;height:118px">
    <div class="art" role="img" aria-label="Drawing of swab collection depth with a timer" style="left:28px;top:30px;width:88px;height:44px"></div>
    <p class="step" style="top:42px">Remove swab from its sterile package and<br>collect a sample from the vagina.</p>
    <div class="notch"></div>
  </div>
  <div class="band band--white" style="top:356px;height:118px">
    <div class="art" role="img" aria-label="Drawing of swab tip placed and snapped into the vial" style="left:28px;top:24px;width:78px;height:64px"></div>
    <p class="step" style="top:46px">Place the swab in the buffer. Break off the swab tip<br>at the scored mark and leave the tip in the vial.</p>
    <div class="notch"></div>
  </div>
  <div class="band band--grey" style="top:474px;height:118px">
    <div class="art" role="img" aria-label="Drawing of the shipping cap replaced on the vial" style="left:28px;top:28px;width:102px;height:60px"></div>
    <p class="step" style="top:52px">Place the shipping cap back on the vial and<br>and return the vial to the lab.</p>
    <div class="notch"></div>
  </div>
  <div class="band band--white" style="top:592px;height:116px">
    <div class="brand" style="left:394px;top:32px"><span>Vela Kit</span><span class="dot"></span></div>
    <div class="brand-sub" style="left:394px;top:62px">Rupture of Membranes Test</div>
    <p class="warning" style="top:68px">Warning:&nbsp; The test may report positive results in patients with intact membranes and therefore decisions to induce labor should not be based solely on the Vela Kit test results.</p>
  </div>
</section>

<section class="sheet sheet--lab" aria-label="Inservice Guide Lab">
  <div class="band band--grey" style="top:0;height:92px">
    <h1 class="title" style="top:46px">Inservice Guide -<strong>Lab</strong></h1>
    <div class="brand" style="left:394px;top:28px"><span>Vela Kit</span><span class="dot"></span></div>
    <div class="brand-sub" style="left:394px;top:58px">Rupture of Membranes Test</div>
    <div class="notch"></div>
  </div>
  <div class="band band--white" style="top:92px;height:91px">
    <div class="art" role="img" aria-label="Drawing of a hand holding the buffer vial upright" style="left:36px;top:14px;width:50px;height:64px"></div>
    <p class="step" style="top:34px">Holding the buffer vial in an upright position,<br>removie the shiping cap as shown</p>
    <div class="notch"></div>
  </div>
  <div class="band band--grey" style="top:183px;height:90px">
    <div class="art" role="img" aria-label="Drawing of the shipping cap swapped for the drop dispenser cap" style="left:28px;top:18px;width:80px;height:56px"></div>
    <p class="step" style="top:38px">Replace shipping cap with drop dispenser cap.</p>
    <div class="notch"></div>
  </div>
  <div class="band band--white" style="top:273px;height:91px">
    <div class="art" role="img" aria-label="Drawing of drops dispensed into the cassette well, four drops" style="left:30px;top:14px;width:82px;height:62px"></div>
    <p class="step" style="top:30px">Place 4 to 6 drops of solution into the well on<br>the test cassette</p>
    <div class="notch"></div>
  </div>
  <div class="band band--grey" style="top:364px;height:90px">
    <div class="art" role="img" aria-label="Drawing of a thumb pressing the cassette timer" style="left:28px;top:12px;width:100px;height:64px"></div>
    <p class="step" style="top:23px">Place test cassette on a flat surface and start<br>timer by pressing with your thumb from the bottom<br>of the timer up</p>
    <div class="notch"></div>
  </div>
  <div class="band band--white" style="top:454px;height:91px">
    <div class="art" role="img" aria-label="Drawing of the cassette with timers showing 5 and 20 minutes" style="left:30px;top:12px;width:100px;height:66px"></div>
    <p class="step" style="top:32px">Wait 20-5 minutes for test<br>result to manifest.</p>
    <div class="notch"></div>
  </div>
  <div class="band band--grey" style="top:545px;height:90px">
    <div class="art" role="img" aria-label="Result windows showing positive, negative and invalid readings" style="left:28px;top:16px;width:136px;height:58px"></div>
    <p class="step" style="top:38px">Read the test result.</p>
  </div>
  <div class="band band--white" style="top:635px;height:73px"></div>
  <p class="foot-links">harbormedica.com | velacheckkit.com</p>
  <p class="foot-info">210 Harbor Loop | Lakeview, Oregon USA 97630 | P. 555-010-2201 | F. 555-010-2202<br>Toll Free: 555-010-2200 | LATEX FREE, DEHP FREE | Made in the USA Patents Pending<br>© Copyright 2014-5 © Harbor Medica, LLC. All rights reserved. P/N <span style="color:var(--green)">XXX-XXXX</span> Rev. A</p>
  <div class="maker"><span class="dot"></span><span>Harbor Medica</span></div>
  <p class="tagline">Trusted in labor and delivery care</p>
</section>

</body>
</html>
```